Business card and stationary for a Real Estate Company.
Bartholomew Quenby
Business card and stationary for a Real Estate Company.  - Real Estate
Creative Brief
Professional
Broker
No address is to appear
bart@quenbyrealestate.example
www.QuenbyRealEstate.example
BRE 04736251
I'm looking for a business card and stationary design for a Real Estate Brokerage. Style is to be simple yet creative. Professional looking with no bold colors. Back of Card: I'd like the logo to appear on the back of the card by itself with no other text. Logo background is to be transparent. Front of Card: There should be no logo or business name just my name at the top with the word Broker immediately below my name. Then my contact information below. I'd like the information to be centered but am open to other ideas. Thank you in advance for your participation
I'd like the logo to appear on the back of the card by itself with no other text. Logo background is to be transparent.

```html
<!DOCTYPE html>
<html lang="en">
<head>
<meta charset="utf-8">
<title>Quenby &amp; Associates — Business Card</title>
<link rel="stylesheet" href="https://fonts.googleapis.com/css2?family=Oswald:wght@500&family=Open+Sans:wght@400;600&display=swap">
<style>
  :root{
    --bg:#e6e6e8;
    --card-white:#ffffff;
    --ink:#1b1b1b;
    --red:#d3202f;
    --grey-text:#5a5a5a;
    --blue-text:#2f4a8a;
    --frame:#111214;
    --panel-top:#fafafa;
    --panel-bottom:#d9d9db;
  }
  *{margin:0;padding:0;box-sizing:border-box}
  html,body{width:1200px;height:869px;overflow:hidden}
  body{background:var(--bg);font-family:"Open Sans",Arial,sans-serif;position:relative}

  .card{position:absolute;width:525px;height:300px;border-radius:6px;box-shadow:0 6px 18px rgba(0,0,0,.18)}

  /* back of card: logo area only */
  .card-back{left:50px;top:284px;background:var(--card-white);display:flex;align-items:center;justify-content:center}
  .brand{display:flex;flex-direction:column;align-items:center;gap:4px}
  .brand-row{display:flex;align-items:center;gap:10px}
  .brand-mark{width:26px;height:26px;background:var(--red)}
  .brand-name{font-family:"Oswald",Arial,sans-serif;font-weight:500;color:var(--ink);font-size:24px;letter-spacing:.5px;text-transform:uppercase}

  /* front of card: name, title, contacts */
  .card-front{left:625px;top:284px;background:var(--frame);padding:14px;border-radius:10px}
  .panel{position:relative;width:100%;height:100%;border-radius:3px;overflow:hidden;
    background:linear-gradient(160deg,var(--panel-top) 0%,#eeeeef 55%,var(--panel-bottom) 100%)}

  .person{position:absolute;left:0;right:0;top:26px;text-align:center}
  .person-name{font-size:18px;letter-spacing:1.5px;color:var(--ink);text-transform:uppercase}
  .person-title{font-size:11px;letter-spacing:3px;color:var(--blue-text);text-transform:uppercase;margin-top:3px}
  .rule{width:60px;height:2px;background:var(--red);margin:10px auto 0}

  .contacts{position:absolute;left:0;right:0;top:96px;list-style:none;display:flex;flex-direction:column;align-items:center;gap:6px}
  .contacts li{display:flex;align-items:center;gap:7px;font-size:10px;color:var(--grey-text)}
  .contacts svg{width:10px;height:10px}
  .icon-fill{fill:var(--blue-text)}
  .icon-line{fill:none;stroke:var(--blue-text);stroke-width:1}

  .swoosh{position:absolute;left:0;bottom:-1px;width:100%;height:111px}
  .swoosh-red{fill:var(--red)}
  .swoosh-white{fill:#ffffff}
  .swoosh-dark{fill:var(--frame)}
  .website{position:absolute;left:34px;bottom:14px;font-size:11px;letter-spacing:2.5px;color:#fff}
</style>
</head>
<body>

<section class="card card-back" aria-label="Back of card">
  <div class="brand">
    <div class="brand-row">
      <span class="brand-mark"></span>
      <span class="brand-name">Quenby &amp; Associates</span>
    </div>
  </div>
</section>

<section class="card card-front" aria-label="Front of card">
  <div class="panel">
    <div class="person">
      <p class="person-name">Bartholomew Quenby</p>
      <p class="person-title">Broker</p>
      <div class="rule"></div>
    </div>

    <ul class="contacts">
      <li><svg viewBox="0 0 10 10"><path class="icon-fill" d="M2 0.5 3.5 2.7 2.6 3.6Q3.6 6 6.4 7.4L7.3 6.5 9.5 8 8.4 9.5Q3 9 0.5 1.6Z"/></svg>010 555 0142</li>
      <li><svg viewBox="0 0 10 10"><path class="icon-line" d="M0.5 2h9v6h-9z M0.5 2 5 5.5 9.5 2"/></svg>bart@quenbyrealestate.example</li>
      <li><svg viewBox="0 0 10 10"><rect class="icon-line" x="0.5" y="1.5" width="9" height="7" rx="0.6"/></svg>BRE 04736251</li>
    </ul>

    <svg class="swoosh" viewBox="0 0 497 111" preserveAspectRatio="none" aria-hidden="true">
      <path class="swoosh-red" d="M0 40 Q140 62 300 70 Q420 76 497 74 L497 111 L0 111Z"/>
      <path class="swoosh-white" d="M0 52 Q160 74 320 80 Q430 84 497 82 L497 111 L0 111Z"/>
      <path class="swoosh-dark" d="M0 58 Q170 80 330 85 Q440 88 497 86 L497 111 L0 111Z"/>
    </svg>
    <p class="website">www.QuenbyRealEstate.example</p>
  </div>
</section>

</body>
</html>
```